2in1 Bartender & Sommelier needs a business card

I need a business card. I worked as a bartender in many places but I just finished a sommelier school and I would like a new business card. I like minimal design, natural materials and something what makes the people think :) I try to be creative in cocktail making, like little mixology, little twist on recipes... I like to travel and discover new places, cultures and of course interesting drinks and improve continously...live a little bit crazy life. And I like what I do...

Target Market(s)

restaurant/winebar managers, winemakers, other sommeliers and bartenders, people who work in food and beverage sector

Industry/Entity Type

Hospitality

Contact Information for Business Card

Rozsa Tarkany
Bartender & Sommelier
Phone: (FR) +33 6 4827 3190
(HU) +36 70 918 6352

Font styles to use
Script

Requirements
Must have
• Some sign, I am a bartender and sommelier as well.
Nice to have
• black and white maybe with 1 or 2 extra color
Should not have
• very colourful, to many things on the card

```html
<!DOCTYPE html>
<html lang="en">
<head>
<meta charset="utf-8">
<title>Rozsa Tarkany – Bartender &amp; Sommelier</title>
<link rel="stylesheet" href="https://fonts.googleapis.com/css2?family=Playball&family=Federo&display=swap">
<style>
  :root {
    --page-bg: #d9d3cb;
    --card-black: #050505;
    --card-charcoal: #1f1f1f;
    --frost: #e9e6e2;
    --burgundy: #6e1a2e;
    --wine: #7d2340;
    --tan: #cdb89f;
  }
  * { margin: 0; padding: 0; box-sizing: border-box; }
  html, body {
    width: 1200px;
    height: 970px;
    overflow: hidden;
    background: var(--page-bg);
  }
  .canvas {
    position: relative;
    width: 1200px;
    height: 970px;
  }
  .business-card {
    position: absolute;
    left: 80px;
    top: 190px;
    width: 1040px;
    height: 590px;
    overflow: hidden;
    background:
      radial-gradient(ellipse 60% 55% at 40% 75%, rgba(60,60,60,0.55), transparent 70%),
      linear-gradient(90deg, var(--frost) 0%, #d8d4cf 14%, #6b6966 20%, var(--card-black) 27%, var(--card-black) 100%);
    box-shadow: 0 10px 30px rgba(0,0,0,0.25);
  }
  .wine-emblem {
    position: absolute;
    left: 0;
    top: 0;
    width: 290px;
    height: 590px;
  }
  .card-name {
    position: absolute;
    left: 430px;
    top: 90px;
    width: 520px;
    text-align: center;
    font-family: "Playball", cursive;
    font-size: 78px;
    line-height: 1;
    color: var(--burgundy);
    letter-spacing: 1px;
  }
  .card-role {
    position: absolute;
    left: 430px;
    top: 198px;
    width: 520px;
    text-align: center;
    font-family: "Federo", sans-serif;
    font-size: 27px;
    color: var(--tan);
    letter-spacing: 0.5px;
  }
  .card-phones {
    position: absolute;
    left: 430px;
    top: 430px;
    width: 520px;
    list-style: none;
    text-align: center;
    font-family: "Federo", sans-serif;
    font-size: 31px;
    line-height: 35px;
    color: var(--tan);
  }
  .phone-country { color: var(--burgundy); }
</style>
</head>
<body>
  <main class="canvas">
    <section class="business-card">
      <svg class="wine-emblem" viewBox="0 0 290 590" role="img" aria-label="Silhouette of a wine glass standing before a wine bottle, in burgundy">
        <defs>
          <linearGradient id="emblemTone" x1="0" y1="0" x2="0" y2="1">
            <stop offset="0" stop-color="#8a2a48"/>
            <stop offset="1" stop-color="#6a1c33"/>
          </linearGradient>
        </defs>
        <rect x="0" y="0" width="290" height="590" fill="url(#emblemTone)" opacity="0.9"/>
      </svg>
      <h1 class="card-name">Rozsa Tarkany</h1>
      <p class="card-role">Bartender &amp; Sommelier</p>
      <ul class="card-phones">
        <li><span class="phone-country">(FR)</span> +33 6 4827 3190</li>
        <li><span class="phone-country">(HU)</span> +36 70 918 6352</li>
      </ul>
    </section>
  </main>
</body>
</html>
```